We have a new logo so we need to change our business card

We're super Happy with our current cards but I think with a new logo should come a new design. I wouldn't mind seeing the icons that we used on the back last time reused on this card. Please feel free to visit our website to get a sense for our brand www.pawlowtide.ca

I need the final final to have contact info for:

Derek Osgood
Co-Owner
info@pawlowtide.ca
604-315-2780

and

Melissa Osgood
Co-Owner
info@pawlowtide.ca
604-347-5138

Target Market(s)

Female dog owners, 21 to 70

Industry/Entity Type

pet industry

Contact Information for Business Card

included in brief

Requirements
Should not have
• We do not want it to look cartonish

```html
<!DOCTYPE html>
<html lang="en">
<head>
<meta charset="utf-8">
<title>Pawlow Tide – Business Card</title>
<link href="https://fonts.googleapis.com/css2?family=Open+Sans:wght@300;400;700;800&family=Poppins:wght@400;600&display=swap" rel="stylesheet">
<style>
  :root{
    --bg:#e6e7e8;
    --paper:#f4f4f2;
    --ink:#151518;
    --green:#8dbb3e;
    --green-soft:#dbe8c4;
    --white:#ffffff;
    --grey-badge:#6b716f;
    --benefit-title:#9a7a52;
    --photo-yellow:#e2d54a;
    --photo-pink:#d9a8cf;
    --wave-brown:#6b5648;
    --wave-purple:#9c6fa3;
    --wave-yellow:#e3d12b;
  }
  *{box-sizing:border-box;margin:0;padding:0}
  html,body{width:1200px;height:1200px;overflow:hidden;background:var(--bg)}
  .sheet{width:1200px;height:1200px;display:flex;flex-direction:column;align-items:center;justify-content:center;gap:44px}
  .card{position:relative;width:900px;height:514px;background:var(--paper);overflow:hidden;box-shadow:0 6px 18px rgba(0,0,0,.15)}
  .card svg.art{position:absolute;inset:0;width:100%;height:100%}

  /* front */
  .brand{position:absolute;left:58px;top:70px;display:flex;align-items:center;gap:22px}
  .brand-dot{width:118px;height:118px;border-radius:50%;background:var(--green)}
  .brand-name{font-family:'Open Sans',sans-serif;font-weight:800;font-size:64px;color:var(--ink);letter-spacing:-1px;line-height:1}
  .person{position:absolute;left:64px;top:330px;color:var(--white);font-family:'Open Sans',sans-serif}
  .person-name{font-size:44px;line-height:1.1}
  .person-name .first{font-weight:300;opacity:.85}
  .person-name .last{font-weight:700}
  .person-role{font-size:26px;font-weight:300;opacity:.55}
  .contacts{position:absolute;left:540px;top:384px;list-style:none;font-family:'Open Sans',sans-serif;font-weight:300;color:var(--white);font-size:28px}
  .contacts li{display:flex;align-items:center;gap:26px;height:40px}
  .contacts .icon{width:30px;height:30px;flex:none}
  .contacts .social-dot{width:28px;height:28px;border-radius:50%;background:var(--white);flex:none;margin-left:1px}

  /* back */
  .benefits{position:absolute;right:40px;top:56px;text-align:right;font-family:'Poppins',sans-serif;color:var(--ink)}
  .benefits h2{font-weight:600;font-size:20px;color:var(--benefit-title);letter-spacing:1px;margin-bottom:4px}
  .benefits ul{list-style:none;font-size:18px;line-height:26px}
  .benefits li::after{content:"";display:inline-block;width:9px;height:9px;border-radius:50%;background:var(--ink);margin-left:12px;vertical-align:middle}
  .benefits li.cont::after{display:none}
  .benefits li.cont{margin-right:21px}
</style>
</head>
<body>
<main class="sheet">

  <!-- front side -->
  <section class="card card-front">
    <svg class="art" viewBox="0 0 900 514" aria-hidden="true">
      <circle class="faint-mark" cx="770" cy="170" r="150" fill="var(--green-soft)" opacity=".6"/>
      <path class="band-green" d="M0,290 C300,240 560,320 900,330 L900,514 L0,514 Z" fill="var(--green)"/>
      <path class="band-black" d="M0,272 C300,222 560,288 900,296 L900,334 C560,326 300,238 0,292 Z" fill="var(--ink)"/>
    </svg>
    <div class="brand">
      <span class="brand-dot"></span>
      <span class="brand-name">Pawlow Tide</span>
    </div>
    <div class="person">
      <p class="person-name"><span class="first">Derek</span> <span class="last">Osgood</span></p>
      <p class="person-role">Co-Owner</p>
    </div>
    <ul class="contacts">
      <li>
        <svg class="icon" viewBox="0 0 30 30"><circle cx="15" cy="15" r="15" fill="var(--white)"/><path d="M10,8 l3,0 l1.5,4 l-2,1.5 a9,9 0 0 0 4,4 l1.5,-2 l4,1.5 l0,3 a2,2 0 0 1 -2,2 a13,13 0 0 1 -12,-12 a2,2 0 0 1 2,-2z" fill="var(--green)"/></svg>
        <span>604-315-2780</span>
      </li>
      <li>
        <svg class="icon" viewBox="0 0 30 30"><circle cx="15" cy="15" r="15" fill="var(--white)"/><rect x="7" y="10" width="16" height="11" fill="none" stroke="var(--green)" stroke-width="1.6"/><path d="M7,10 L15,17 L23,10" fill="none" stroke="var(--green)" stroke-width="1.6"/></svg>
        <span>info@pawlowtide.ca</span>
      </li>
      <li>
        <span class="social-dot"></span>
        <span>pawlowtide</span>
      </li>
    </ul>
  </section>

  <!-- back side -->
  <section class="card card-back">
    <svg class="art" viewBox="0 0 900 514">
      <defs>
        <linearGradient id="photoTone" x1="0" y1="0" x2="1" y2="0.3">
          <stop offset="0" stop-color="var(--photo-yellow)"/>
          <stop offset="0.5" stop-color="var(--photo-pink)"/>
          <stop offset="1" stop-color="var(--paper)"/>
        </linearGradient>
        <linearGradient id="waveTone" x1="0" y1="0" x2="1" y2="0">
          <stop offset="0" stop-color="var(--wave-brown)"/>
          <stop offset="0.45" stop-color="var(--wave-purple)"/>
          <stop offset="1" stop-color="var(--wave-yellow)"/>
        </linearGradient>
      </defs>
      <path class="product-photo" role="img" aria-label="Photo of stacked product sachets in yellow and pink packaging"
            d="M0,0 H480 C450,80 410,140 350,190 C240,175 120,165 0,168 Z" fill="url(#photoTone)"/>
      <path class="wave-line" d="M0,170 C250,170 420,300 600,370 C720,415 820,425 900,420" fill="none" stroke="url(#waveTone)" stroke-width="7"/>
      <g class="badges" fill="var(--grey-badge)">
        <circle cx="100" cy="360" r="56"/>
        <circle cx="245" cy="405" r="42" fill="none" stroke="var(--grey-badge)" stroke-width="4"/>
        <circle cx="385" cy="430" r="42"/>
        <circle cx="525" cy="452" r="42"/>
        <circle cx="665" cy="466" r="40"/>
        <circle cx="805" cy="474" r="34" fill="none" stroke="var(--grey-badge)" stroke-width="6"/>
      </g>
    </svg>
    <div class="benefits">
      <h2>BENEFITS</h2>
      <ul>
        <li>Improves condition of the skin and fur</li>
        <li>Reduces shedding and dandruff</li>
        <li>Strengthens the immune system</li>
        <li>Helps eliminate unwanted odours</li>
        <li>Adds a scented benefit</li>
        <li class="cont">Helps with; anxiety, arthritis, insomnia</li>
        <li>drowsiness, skin irritation &amp; depression</li>
      </ul>
    </div>
  </section>

</main>
</body>
</html>
```